The Harlow Law Firm, PC

Dwight K. Harlow
Attorney at Law
physical address: 287 E. 9th Avenue
Corvale, EX 27019

mailing: P.O. Box 5843
Corvale, EX 27021

o. 555.416.2071
f. 555.416.8532

www.harlowlegal-ex.com

Industry/Entity Type

Attorney

Contact Information for Business Card

Attorney name
Office Phone number
Office Fax number
Mailing address and physical address
website address

Requirements
Must have
• Clean fresh design - I hate the website

```html
<!DOCTYPE html>
<html lang="en">
<head>
<meta charset="utf-8">
<title>Harlow Law Firm – Business Card</title>
<link rel="stylesheet" href="https://fonts.googleapis.com/css2?family=Cabin:wght@400;600&display=swap">
<style>
  :root {
    --backdrop: #d8d3cc;
    --card: #ffffff;
    --accent: #b5571b;
    --ink: #1a1a1a;
  }
  * { margin: 0; padding: 0; box-sizing: border-box; }
  html, body {
    width: 1200px;
    height: 900px;
    overflow: hidden;
    background: var(--backdrop);
    font-family: "Cabin", "Gill Sans", sans-serif;
  }
  .card {
    position: absolute;
    left: 100px;
    top: 164px;
    width: 1000px;
    height: 572px;
    background: var(--card);
    border-radius: 16px;
    box-shadow: 0 6px 18px rgba(0, 0, 0, 0.18);
  }
  .firm-name {
    position: absolute;
    left: 58px;
    top: 70px;
    font-size: 62px;
    font-weight: 400;
    color: var(--accent);
    letter-spacing: 0.5px;
  }
  .attorney {
    position: absolute;
    left: 440px;
    top: 178px;
    width: 300px;
    text-align: center;
  }
  .attorney-name {
    font-size: 27px;
    font-weight: 600;
    color: var(--accent);
  }
  .attorney-title {
    font-size: 17px;
    color: var(--ink);
  }
  .divider {
    position: absolute;
    left: 0;
    top: 262px;
    width: 100%;
    height: 2px;
    background: var(--accent);
  }
  .contact {
    position: absolute;
    left: 0;
    top: 296px;
    display: grid;
    grid-template-columns: 290px auto;
    column-gap: 16px;
    row-gap: 10px;
    font-size: 25px;
    line-height: 32px;
  }
  .contact dt {
    text-align: right;
    color: var(--accent);
  }
  .contact dd {
    color: var(--ink);
  }
</style>
</head>
<body>
  <article class="card">
    <h1 class="firm-name">Harlow Law Firm</h1>
    <div class="attorney">
      <p class="attorney-name">Dwight K. Harlow</p>
      <p class="attorney-title">Attorney at Law</p>
    </div>
    <div class="divider"></div>
    <dl class="contact">
      <dt>Address</dt><dd>287 E. 9th Avenue, Corvale, EX 27019</dd>
      <dt>Mailing Address</dt><dd>P.O. Box 5843 Corvale, EX 27021</dd>
      <dt>Office</dt><dd>555.416.2071</dd>
      <dt>Fax</dt><dd>555.416.8532</dd>
      <dt>Website</dt><dd>www.harlowlegal-ex.com</dd>
    </dl>
  </article>
</body>
</html>
```